Zielgruppe
Wir sind ein kleiner familiengeführter Weinbaubetrieb am Wagram und suchen einen modernen und naturnahen Namen und ein Etikett mit Blickfang für unseren Wermut, aus handgepflückten regionalen Wildkräutern mit Rosewein vom Zweigelt. Charakeristik des Getränks: Aperitif, Zitrusnote, leichte Bitternote, mit Tonic water als Cocktail.
Unsere Zielgruppe: kaufkräftige Genussmenschen im mittleren Alter
Aufgabenstellung
Etikett für 0,5l Flasche, Flasche noch nicht festgelegt, Etikettenhöhe: 65mm
Was soll draufstehen: Name, Vermouth, local botanicals, handcrafted, small batch

```html
<!DOCTYPE html>
<html lang="en">
<head>
<meta charset="utf-8">
<title>Steinkrauter Vermouth – Label</title>
<link rel="stylesheet" href="https://fonts.googleapis.com/css2?family=Encode+Sans+Semi+Condensed:wght@400&family=Bitter:wght@800&family=Quattrocento:wght@400&display=swap">
<style>
  :root {
    --page-bg: #e4e5e9;
    --label-white: #ffffff;
    --wash-blush: #f3dde1;
    --wash-pink: #dcaab4;
    --wash-rose: #b8707f;
    --wash-wine: #93394f;
    --wash-deep: #6a1630;
    --wash-darkest: #4e0c20;
    --ink: #141414;
    --band-black: #050505;
    --text-light: #f4f1ef;
  }
  * { margin: 0; padding: 0; box-sizing: border-box; }
  html, body {
    width: 1200px;
    height: 1020px;
    overflow: hidden;
    background: var(--page-bg);
  }
  .canvas {
    position: relative;
    width: 1200px;
    height: 1020px;
  }
  .label {
    position: absolute;
    left: 120px;
    top: 143px;
    width: 960px;
    height: 734px;
    overflow: hidden;
    background: var(--label-white);
    box-shadow: 0 6px 18px rgba(0, 0, 0, 0.12);
  }
  .label__wash {
    position: absolute;
    left: 0;
    top: 0;
    width: 960px;
    height: 643px;
  }
  .label__name {
    position: absolute;
    top: 30px;
    left: 0;
    width: 100%;
    text-align: center;
    font-family: "Encode Sans Semi Condensed", sans-serif;
    font-weight: 400;
    font-size: 98px;
    line-height: 1;
    letter-spacing: -1px;
    color: var(--ink);
  }
  .label__illustration {
    position: absolute;
    left: 253px;
    top: 150px;
    width: 450px;
    height: 493px;
  }
  .label__product {
    position: absolute;
    top: 580px;
    left: 0;
    width: 100%;
    text-align: center;
    font-family: "Bitter", serif;
    font-weight: 800;
    font-size: 58px;
    line-height: 1;
    letter-spacing: 1px;
    color: var(--text-light);
  }
  .label__band {
    position: absolute;
    left: 0;
    bottom: 0;
    width: 100%;
    height: 91px;
    background: var(--band-black);
    display: flex;
    align-items: center;
    justify-content: center;
  }
  .label__claims {
    font-family: "Quattrocento", serif;
    font-weight: 400;
    font-size: 42px;
    line-height: 1;
    color: var(--text-light);
    white-space: nowrap;
  }
</style>
</head>
<body>
  <main class="canvas">
    <section class="label">
      <svg class="label__wash" viewBox="0 0 960 643" preserveAspectRatio="none" aria-hidden="true">
        <defs>
          <filter id="wash-soft" x="-10%" y="-20%" width="120%" height="140%">
            <feGaussianBlur stdDeviation="10"/>
          </filter>
          <filter id="wash-softer" x="-10%" y="-20%" width="120%" height="140%">
            <feGaussianBlur stdDeviation="18"/>
          </filter>
        </defs>
        <g class="wash-layers">
          <path filter="url(#wash-softer)" fill="var(--wash-blush)" d="M-40 300 C 20 270, 70 285, 120 282 C 180 278, 230 300, 300 296 C 380 292, 440 278, 520 290 C 600 300, 650 268, 720 280 C 790 292, 840 262, 900 276 C 940 286, 980 300, 1000 320 L 1000 700 L -40 700 Z"/>
          <path filter="url(#wash-soft)" fill="var(--wash-pink)" d="M-40 330 C 30 318, 80 340, 150 326 C 220 312, 270 352, 340 342 C 420 330, 470 362, 560 350 C 640 340, 690 372, 760 352 C 830 334, 880 364, 930 372 C 960 376, 990 380, 1000 386 L 1000 700 L -40 700 Z"/>
          <path filter="url(#wash-soft)" fill="var(--wash-rose)" d="M-40 392 C 40 378, 90 406, 170 396 C 250 386, 300 418, 380 408 C 460 398, 520 430, 600 418 C 680 406, 740 438, 820 424 C 880 414, 930 440, 1000 446 L 1000 700 L -40 700 Z"/>
          <path filter="url(#wash-soft)" fill="var(--wash-wine)" d="M-40 468 C 50 456, 110 486, 190 474 C 270 462, 330 494, 410 484 C 500 474, 560 502, 640 490 C 720 478, 790 506, 860 494 C 920 484, 960 500, 1000 506 L 1000 700 L -40 700 Z"/>
          <path filter="url(#wash-soft)" fill="var(--wash-deep)" d="M-40 540 C 60 530, 130 556, 220 546 C 320 536, 380 562, 470 552 C 570 542, 640 566, 740 556 C 830 546, 900 566, 1000 572 L 1000 700 L -40 700 Z"/>
          <path filter="url(#wash-soft)" fill="var(--wash-darkest)" d="M-40 604 C 80 596, 180 616, 300 608 C 420 600, 520 618, 640 610 C 760 602, 880 618, 1000 614 L 1000 700 L -40 700 Z"/>
        </g>
      </svg>
      <h1 class="label__name">STEINKRAUTER</h1>
      <svg class="label__illustration" viewBox="0 0 450 493" role="img" aria-label="Engraved illustration of a lizard on rocks among grass">
        <defs>
          <radialGradient id="illustration-tone" cx="50%" cy="48%" r="50%">
            <stop offset="0%" stop-color="#2a1a1e" stop-opacity="0.28"/>
            <stop offset="60%" stop-color="#3a2a2e" stop-opacity="0.12"/>
            <stop offset="100%" stop-color="#3a2a2e" stop-opacity="0"/>
          </radialGradient>
        </defs>
        <ellipse cx="225" cy="240" rx="215" ry="235" fill="url(#illustration-tone)"/>
      </svg>
      <p class="label__product">VERMOUTH</p>
      <div class="label__band">
        <p class="label__claims">local botanicals - handcrafted - small batch</p>
      </div>
    </section>
  </main>
</body>
</html>
```